International Internship Provider Needs Catalogue Layout & Design

We need a catalogue/booklet created to send out to university students and study abroad offices. We provide international internships to university students and young professionals in a range of fields in nine cities across the globe. Our program includes guaranteed internship, accommodation, social events, and support from staff. We would like to provide a clean, glossy, and picture-heavy publication to promote our program and website. We'd like to use captivating colors and the final product should convey what our program does and express the fun of living abroad with the professionalism of an internship.

Reason: We've increased the budget by $100, and we understand the project is a large undertaking. Thank you!

We would like each location to be two pages with large images of that location as well as all of the copy in the word document attached. Attached on the images is as an example of another catalogue we liked the style of for you to look at it. If you need any more details or would like me to break up the copy into sections please do not hesitate to ask. thank you!  

I've added new file of content that includes everything in the previous file plus more information, but on separate pages to help make it clear what information goes together. The location should still be a two-page spread that includes a large location image. We would like to have a quote from a student on each of those pages as well. 

I've added more photos for the location pages labeled by the location (ex: London_girls). I've also added some photos for Project Kelvo and new content. Please contact me with any questions. 

Reason: We realized we've asked for a few more edits from designers and we appreciate the time it takes to be make these constant edits. Thank you!

University students and recent college graduates. Usually the target market is between 21-23 years of age, and most students who travel abroad are female.

University

• It must be at least 10 pages and use the logo I've attached. Please be sure to look at the word document that is full of content that will be used in the project. Large photos of the locations are ideal as well 2 pages for each location.
• I have loads of photos I can give to you to use in the document, but you can use placeholders for now or some of the photos I've attached. I've also included a document full of copy that will need to be in the document just to give you an idea of where things will be displayed.

```html
<!DOCTYPE html>
<html lang="en">
<head>
<meta charset="utf-8">
<title>London, England – Program Spread</title>
<link href="https://fonts.googleapis.com/css2?family=Source+Sans+3:wght@400;600;700&display=swap" rel="stylesheet">
<style>
  :root {
    --navy: #1d4f73;
    --title-blue: #1f5d8c;
    --ink: #1a1a1a;
    --body-ink: #2b2b2b;
    --rule: #3a6f99;
    --green: #8cc63f;
    --green-light: #c9e39b;
    --slate: #7e8bab;
    --slate-light: #e9ecf3;
    --white: #ffffff;
  }
  * { box-sizing: border-box; margin: 0; padding: 0; }
  html, body { width: 1200px; height: 464px; overflow: hidden; background: var(--white); }
  body { font-family: "Source Sans 3", Arial, sans-serif; color: var(--ink); }
  .spread { position: relative; width: 1200px; height: 464px; }

  .bar { position: absolute; height: 5px; background: var(--navy); }
  .bar.top-left { left: 15px; width: 570px; top: 13px; }
  .bar.top-right { left: 615px; width: 570px; top: 13px; }
  .bar.bottom-left { left: 15px; width: 570px; top: 446px; }
  .bar.bottom-right { left: 615px; width: 570px; top: 446px; }

  .side-tab { position: absolute; top: 78px; width: 22px; height: 307px; background: var(--navy); }
  .side-tab.left { left: 0; border-radius: 0 10px 10px 0; }
  .side-tab.right { right: 0; border-radius: 10px 0 0 10px; }

  .page-title { position: absolute; left: 44px; top: 30px; font-size: 31px; font-weight: 400; color: var(--title-blue); letter-spacing: 0.2px; }
  .intro { position: absolute; left: 44px; top: 84px; width: 306px; font-size: 9.3px; line-height: 15px; }

  .feature-list { position: absolute; left: 58px; list-style: none; font-size: 9px; line-height: 11px; }
  .feature-list li { position: relative; padding-left: 7px; }
  .feature-list li::before { content: "•"; position: absolute; left: 0; }
  .feature-list.primary { top: 173px; }
  .feature-list.secondary { top: 262px; }
  .divider { position: absolute; left: 46px; top: 248px; width: 310px; height: 1px; background: var(--rule); }

  .social-events { position: absolute; left: 47px; top: 344px; width: 313px; height: 102px; }
  .social-events h2 { height: 31px; padding: 6px 0 0 16px; font-size: 16px; font-weight: 400; color: var(--ink);
    background: linear-gradient(180deg, var(--white) 0%, var(--green-light) 45%, var(--green) 100%); border-radius: 0 10px 0 0; }
  .social-events ul { list-style: none; height: 71px; padding: 7px 0 0 12px; font-size: 13.5px; line-height: 16px; color: var(--navy);
    background: linear-gradient(180deg, var(--slate) 0%, var(--slate-light) 100%); }
  .social-events li::before { content: "• "; }

  .column-rule { position: absolute; left: 374px; top: 28px; width: 1px; height: 412px; background: var(--rule); }

  .promo { position: absolute; left: 390px; top: 36px; width: 188px; height: 254px; padding: 21px 22px 0 14px;
    background: linear-gradient(180deg, var(--slate) 0%, #b3bccf 45%, var(--white) 100%); }
  .promo h3 { font-size: 13px; font-weight: 700; line-height: 16px; margin-bottom: 2px; color: var(--white); padding-right: 6px; }
  .promo p { font-size: 9.2px; line-height: 18.5px; color: var(--body-ink); }

  .photo-fill { position: absolute; }
  .photo-fill.group { left: 390px; top: 313px; width: 188px; height: 124px;
    background: linear-gradient(180deg, #c9ced6 0%, #9aa3ad 50%, #5f7a4a 100%); }
  .photo-fill.hero { left: 617px; top: 28px; width: 566px; height: 407px;
    background: linear-gradient(180deg, #d7d9db 0%, #8f9291 40%, #4d4f4f 75%, #6f7d5a 100%); }

  .photo-frame { position: absolute; left: 631px; width: 155px; background: var(--white); border: 1px solid var(--ink);
    display: flex; align-items: center; justify-content: center; font-size: 11px; font-weight: 700; }
  .photo-frame.upper { top: 42px; height: 131px; }
  .photo-frame.lower { top: 186px; height: 239px; }

  .speech { position: absolute; left: 930px; top: 28px; width: 255px; height: 260px; }
  .quote { position: absolute; left: 958px; top: 113px; width: 214px;
    font-size: 9.3px; line-height: 11.5px; color: var(--white); text-align: center; }
  .quote cite { display: block; font-style: normal; text-align: right; padding-right: 52px; }
</style>
</head>
<body>
<div class="spread">
  <div class="bar top-left"></div>
  <div class="bar top-right"></div>
  <div class="bar bottom-left"></div>
  <div class="bar bottom-right"></div>
  <div class="side-tab left"></div>
  <div class="side-tab right"></div>

  <h1 class="page-title">London, England</h1>
  <p class="intro">London is recognized as one of the most international and influential cities in the world. Walk along the bustling streets where the past and future seamlessly flow around modern architecture and historic cathedrals. The city is full of thousands of opportunities in every field and an internship in London will be sure to catch an employer’s eye.</p>

  <ul class="feature-list primary">
    <li>Spring and Fall 15 week programs</li>
    <li>Spring and Fall 12-15 credit 15 week program</li>
    <li>Summer 8 week program (two start dates)</li>
    <li>Inclusions</li>
    <li>Guaranteed internship</li>
    <li>Centralized group student-residence style housing, Zone 1-2</li>
  </ul>
  <div class="divider"></div>
  <ul class="feature-list secondary">
    <li>Individualized career development and<br>pre-departure support</li>
    <li>Medical/travel insurance</li>
    <li>Local staff support in London</li>
    <li>Mobile Phone</li>
    <li>Academic Internship Program in London</li>
  </ul>

  <section class="social-events">
    <h2>Social Events</h2>
    <ul>
      <li>Trip to Stonehenge</li>
      <li>Walking tour around London</li>
      <li>Trip to Bath and Oxford</li>
    </ul>
  </section>

  <div class="column-rule"></div>

  <aside class="promo">
    <h3>Do you want to want to study and intern abroad this year?</h3>
    <p>Spend your fall or spring semester living, studying and interning in London for 15 weeks. Through our partnership with the Northgate Education Trust we can offer university student the opportunity to earn up to 15 credit hours from Halvern University and gain hands-on internship experience.</p>
  </aside>

  <div class="photo-fill group" role="img" aria-label="Photo of students jumping on a lawn in front of Big Ben and Parliament"></div>

  <div class="photo-fill hero" role="img" aria-label="Photo of a student sitting beneath a large bronze lion statue in Trafalgar Square"></div>

  <div class="photo-frame upper">photo</div>
  <div class="photo-frame lower">photo</div>

  <svg class="speech" viewBox="0 0 255 260" aria-hidden="true">
    <defs>
      <linearGradient id="bubble-green" x1="1" y1="0" x2="0" y2="1">
        <stop offset="0" stop-color="#7dbb35"/>
        <stop offset="0.55" stop-color="#a9d66c"/>
        <stop offset="1" stop-color="#e2f1c9"/>
      </linearGradient>
    </defs>
    <path d="M55 247 C85 205 110 188 150 174 C205 168 242 145 238 110 C234 82 200 68 168 78 C150 140 112 192 55 247 Z" fill="url(#bubble-green)"/>
    <path d="M212 3 C165 28 95 40 52 60 C14 80 14 140 58 160 C105 180 195 172 222 134 C240 106 214 62 212 3 Z" fill="var(--navy)"/>
  </svg>
  <blockquote class="quote">
    “I think my internship<br>in London helped me get my foot<br>in the door. During my time in London<br>I did a lot of networking and that was key.<br>I got to showcase my talent and I learned a<br>lot as well.”
    <cite>–Maren, London intern,<br>Westbrook College</cite>
  </blockquote>
</div>
</body>
</html>
```